Billboard Design for Modern Dispensary

Hello!
We need a eye-catching 12' x 24' billboard designed for a very successful, modern cannabis dispensary on the Oregon coast, United States. Because of rules, we cannot have any marijuana leafs or other cannabis related images (flower, joints, smoke, etc). We can use the words "Shop" or "Dispensary" - we cannot use the words "cannabis", "marijuana".

Some ideas we had are 3 words stacked on left or center of billboard - maybe across bottom we have horizontal logo and the following words - “South of bridge in Marlow Cove”
Another idea is to have a small bubble in bottom/top corner with image of our dog (face only) - with some words around it - like "BONUS Shop Dog" or "Cute Shop Dog" or "Best Shop Dog" or "Friendly Staff"

here's some 3 word examples:
ENJOY
YOUR
TRIP

or

FEEL
GOOD
JUST
AHEAD

or

GOOD
VIBES
ONLY

or

GOOD
TIMES
CHILL
VIBES

I have attached our logo. I have also included a stacked logo version (vertical, not horizontal). the formats are .EPS and .PDF - the logos were created in Affinity Design 2.x.

Our website is lunarwharf.com if you want to see more images, etc about our dispensary.

Artwork Requirements:
The billboard is 12' tall x 25' wide
The artwork needs to be 1”=1’ @ 300dpi
Please add 6” of bleed all around so your total artwork is 13”x26”
Final deliverable should be .Ai file.

Font styles to use
Sans Serif

Colors
0054AA
0677BA
7BADD7
CADEEF
E8F1F8

Requirements
Nice to have
• See the project description - we included some ideas to consider.
Should not have
• No cannabis images, like flower, cannabis leaves, paraphenlia, cartridges, joints, etc.

```html
<!DOCTYPE html>
<html lang="en">
<head>
<meta charset="utf-8">
<title>Lunar Wharf Billboard</title>
<link href="https://fonts.googleapis.com/css2?family=Poppins:wght@400;500;700;800&display=swap" rel="stylesheet">
<style>
  :root {
    --brand-blue: #4d9cd6;
    --ink: #2b2323;
    --paper: #ffffff;
    --guide: #cfcfcf;
    --guide-text: #a9a9a9;
    --photo-dark: #4a3a30;
    --photo-light: #d9c3a0;
  }
  * { box-sizing: border-box; margin: 0; padding: 0; }
  html, body { width: 1200px; height: 1200px; overflow: hidden; background: var(--paper); }
  body { position: relative; font-family: "Poppins", sans-serif; }

  .spec-sheet { position: absolute; left: 0; top: 0; width: 1200px; height: 600px; background: var(--paper); }
  .guide { position: absolute; background: var(--guide); }
  .guide--h { height: 1px; left: 174px; width: 850px; }
  .guide--v { width: 1px; top: 72px; height: 455px; }
  .measure {
    position: absolute; font-size: 15px; color: var(--guide-text);
    font-family: "Poppins", sans-serif; letter-spacing: 0.05em;
  }
  .measure--top { left: 582px; top: 82px; }
  .measure--bottom { left: 582px; top: 497px; }
  .measure--side { top: 290px; transform: rotate(-90deg); }
  .measure--left { left: 186px; }
  .measure--right { left: 996px; }

  .showcase { position: absolute; left: 0; top: 600px; width: 1200px; height: 600px; background: var(--brand-blue); }

  .billboard {
    position: absolute; left: 220px; width: 760px; height: 365px;
    background: var(--paper); overflow: hidden;
  }
  .spec-sheet .billboard { top: 117px; }
  .showcase .billboard { top: 118px; }

  .billboard__shapes { position: absolute; inset: 0; }
  .billboard__headline {
    position: absolute; left: 33px; top: 18px;
    font-weight: 700; font-size: 62px; line-height: 60px;
    color: var(--brand-blue); letter-spacing: -0.005em;
  }
  .billboard__tagline {
    position: absolute; left: 34px; top: 210px;
    font-size: 14.5px; font-weight: 400; color: var(--ink); letter-spacing: 0.04em;
  }
  .brand-mark {
    position: absolute; left: 34px; top: 283px;
    display: flex; align-items: center; gap: 6px;
  }
  .brand-mark__dot {
    width: 46px; height: 46px; border-radius: 50%;
    border: 3px solid var(--brand-blue); background: var(--paper);
  }
  .brand-mark__name { font-size: 21px; font-weight: 500; color: var(--brand-blue); letter-spacing: 0.01em; }

  .shop-dog {
    position: absolute; left: 515px; top: 32px;
    width: 214px; height: 214px; border-radius: 50%;
    border: 4px solid var(--brand-blue);
    background: radial-gradient(circle at 55% 45%, var(--photo-light) 0%, #c8ad86 45%, var(--photo-dark) 100%);
  }
  .shop-dog__caption {
    position: absolute; left: 522px; top: 256px; width: 200px; text-align: center;
    font-size: 19.5px; font-weight: 700; color: var(--ink);
  }
</style>
</head>
<body>
  <section class="spec-sheet">
    <div class="guide guide--h" style="top:117px"></div>
    <div class="guide guide--h" style="top:482px"></div>
    <div class="guide guide--v" style="left:220px"></div>
    <div class="guide guide--v" style="left:980px"></div>
    <span class="measure measure--top">25 "</span>
    <span class="measure measure--bottom">25 "</span>
    <span class="measure measure--side measure--left">12 "</span>
    <span class="measure measure--side measure--right">12 "</span>

    <div class="billboard">
      <svg class="billboard__shapes" width="760" height="365" viewBox="0 0 760 365" aria-hidden="true">
        <circle cx="260" cy="0" r="50" fill="var(--brand-blue)"/>
        <circle cx="374" cy="408" r="112" fill="var(--brand-blue)"/>
        <circle cx="659" cy="360" r="37" fill="var(--brand-blue)"/>
        <circle cx="718" cy="306" r="16" fill="var(--brand-blue)"/>
      </svg>
      <h1 class="billboard__headline">BEST<br>DISPENSARY<br>PERIOD</h1>
      <p class="billboard__tagline">South of bridge in Marlow Cove</p>
      <div class="brand-mark"><span class="brand-mark__dot"></span><span class="brand-mark__name">LUNAR WHARF</span></div>
      <div class="shop-dog" role="img" aria-label="Photo of the smiling shop dog wearing a bandana"></div>
      <p class="shop-dog__caption">BEST SHOP DOG</p>
    </div>
  </section>

  <section class="showcase">
    <div class="billboard">
      <svg class="billboard__shapes" width="760" height="365" viewBox="0 0 760 365" aria-hidden="true">
        <circle cx="260" cy="0" r="50" fill="var(--brand-blue)"/>
        <circle cx="374" cy="408" r="112" fill="var(--brand-blue)"/>
        <circle cx="659" cy="360" r="37" fill="var(--brand-blue)"/>
        <circle cx="718" cy="306" r="16" fill="var(--brand-blue)"/>
      </svg>
      <h2 class="billboard__headline">BEST<br>DISPENSARY<br>PERIOD</h2>
      <p class="billboard__tagline">South of bridge in Marlow Cove</p>
      <div class="brand-mark"><span class="brand-mark__dot"></span><span class="brand-mark__name">LUNAR WHARF</span></div>
      <div class="shop-dog" role="img" aria-label="Photo of the smiling shop dog wearing a bandana"></div>
      <p class="shop-dog__caption">BEST SHOP DOG</p>
    </div>
  </section>
</body>
</html>
```